Brill's Jewelers website (www.brillsjewelers-example.com)

We are in need of a web storefront for a retail Jewelry store.
www.brillsjewelers-example.com
https://www.facebook.com/Brills-Jewelers-Palm-Vista-740315928461257/

Brill's Jewelers is located in Palm Vista, Florida. The store has been family owned and operated since 1958. Their focus customers are high-income families that care about quality over the brand name. They mostly sell fashion jewelry and diamonds up to 8 carats. We are looking for a simple minimalistic site that their customers can view their inventory and purchase items online.

Competitors websites:
https://www.orvinjewelers-example.com/
http://www.pelvaro-example.com/
http://truecutjewelers-example.com/

Pages:
-Home (with message bulletin)
-Jewelry
We would be able to create the subpages ie Rings, Bracelets, Earrings, Necklaces, Estate, Watches, Men's, Children's
-Services
We would need sub pages ie Appraisals, Consignment, Repairs
-About us
-Contact

Target Market(s)

Local wealthy families

Coding

Number of Pages Required

Font styles to use
Serif

Requirements
Must have
• -An E-commerce site customers can buy jewelry online.
-An easy process internally to add new items to the site
-Colors are Black and White or Black and Gold
Nice to have
• I would like to stay away from face shots of random models in stock photos. I want the jewelry pieces as the focus, not models.

```html
<!DOCTYPE html>
<html lang="en">
<head>
<meta charset="utf-8">
<title>Brill's Jewelers</title>
<link href="https://fonts.googleapis.com/css2?family=Lato:wght@400;700&family=Libre+Baskerville&family=Poppins:wght@600;700&family=Montserrat:wght@400;500;700&display=swap" rel="stylesheet">
<style>
:root{
  --gold:#a98436;
  --gold-light:#c9a24f;
  --black:#0b0b0b;
  --dark:#262626;
  --darker:#1b1b1b;
  --text:#333;
  --muted:#777;
  --line:#e4e4e4;
  --paper:#fafaf7;
  --soft:#f2f2f2;
  --white:#fff;
}
*{box-sizing:border-box;margin:0;padding:0}
html,body{width:1200px;height:3403px;overflow:hidden}
body{font-family:"Lato",sans-serif;color:var(--text);background:var(--white);font-size:14px}
a{color:inherit;text-decoration:none}
.wrap{width:1000px;margin:0 auto;position:relative}

/* Top bar */
.topbar{height:100px;background:var(--paper);border-bottom:1px solid var(--line)}
.topbar .wrap{display:flex;align-items:center;justify-content:space-between;height:100%}
.topbar .contact{font-size:12.5px;color:#444;width:330px}
.brand{text-align:center}
.brand-name{font-family:"Montserrat",sans-serif;font-weight:500;font-size:26px;color:#111;line-height:1}
.brand-tag{font-family:"Montserrat",sans-serif;font-weight:400;font-size:9px;letter-spacing:1px;margin-top:6px;color:#555}
.account{font-size:12.5px;color:#555;display:flex;gap:10px;width:330px;justify-content:flex-end}
.account span+span{border-left:1px solid #ccc;padding-left:10px}

/* Nav */
.nav{height:63px;background:var(--paper);border-bottom:1px solid var(--line)}
.nav .wrap{display:flex;align-items:center;height:100%}
.nav ul{list-style:none;display:flex}
.nav li{font-family:"Montserrat",sans-serif;font-size:13px;color:#222;margin-right:43px}
.nav li:first-child{margin-left:30px}
.caret{display:inline-block;border:4px solid transparent;border-top:5px solid #222;border-bottom:0;margin-left:5px;vertical-align:2px}
.nav .tools{margin-left:auto;display:flex;align-items:center;gap:8px;font-size:11.5px;color:#222}
.nav .tools i{width:1px;height:12px;background:#bbb;display:block}

/* Hero */
.hero{height:512px;background:var(--black);position:relative}
.hero-art{position:absolute;left:128px;top:105px;width:400px;height:345px;border-radius:40%;background:radial-gradient(ellipse at center,#d7d7d7 0%,#8a8a8a 45%,#0b0b0b 72%)}
.hero-copy{position:absolute;left:614px;top:170px}
.hero-copy h1{font-family:"Poppins",sans-serif;font-weight:700;font-size:37px;line-height:56px;color:#fff;letter-spacing:.5px}
.btn-outline{display:inline-block;margin-top:28px;border:1px solid #fff;color:#fff;padding:15px 23px;font-size:19px}
.arrow{position:absolute;top:224px;width:45px;height:60px;background:var(--gold);display:flex;align-items:center;justify-content:center}
.arrow.left{left:0}.arrow.right{right:0}

/* Section title */
.sec-title{text-align:center}
.sec-title h2{font-family:"Libre Baskerville",serif;font-weight:400;font-size:17px;letter-spacing:1px;color:#222}
.stars{display:flex;align-items:center;justify-content:center;gap:6px;margin-top:6px}
.stars:before,.stars:after{content:"";width:50px;height:1px;background:#333}
.stars svg{display:block}
.light .sec-title h2{color:#fff}
.light .stars:before,.light .stars:after{background:#fff}

/* About */
.about{height:507px;padding-top:60px}
.about-body{display:flex;margin-top:48px;gap:27px}
.about-photo{width:486px;height:300px;background:linear-gradient(135deg,#e8e3dc 0%,#bdb5aa 45%,#3a2c26 70%,#d9d3cb 100%)}
.about-text{width:490px;font-family:"Montserrat",sans-serif;font-size:15px;line-height:24px;color:#333;padding-top:18px}
.about-text p{margin-bottom:17px}
.btn-gold{display:inline-block;background:var(--gold);color:#fff;padding:13px 31px;font-size:15px;margin-top:18px}

/* Products */
.showcase{height:530px;background:var(--soft);padding-top:52px}
.product-row{display:flex;gap:18px;width:1028px;margin:48px auto 0}
.product{width:243px;height:309px;background:#fff}
.product-img{height:243px;width:243px;background:radial-gradient(circle at center,#d5d5d5 0%,#f3f3f3 40%,#fff 62%)}
.product-img.gold{background:radial-gradient(circle at center,#e8c860 0%,#d9b240 35%,#fff 50%)}
.product-info{display:flex;justify-content:space-between;padding:8px 11px 0}
.product-name{font-family:"Montserrat",sans-serif;font-size:13px;color:#555;line-height:18px}
.product-price{font-family:"Montserrat",sans-serif;font-weight:500;font-size:16px;color:#111;text-align:right}
.product-price s{display:block;font-size:11px;color:#999}
.rating{color:var(--gold);font-size:11px;letter-spacing:1px;padding:2px 11px 0}

/* Services */
.services{height:439px;background:radial-gradient(ellipse at 62% 50%,#3a3530 0%,#151414 40%,#050505 75%);padding-top:56px}
.service-row{display:flex;gap:61px;width:969px;margin:44px auto 0;position:relative;left:-12px}
.service{width:197px;text-align:center}
.service-box{width:197px;height:155px;border:1px solid var(--gold);display:flex;align-items:center;justify-content:center;background:rgba(0,0,0,.35)}
.service h3{font-weight:400;color:#fff;font-size:19px;margin-top:25px;letter-spacing:.3px}

/* Bridal */
.bridal{height:794px;background:linear-gradient(180deg,#f4f4f4 0%,#d9d9d9 40%,#e6e6e6 70%,#9a9a9a 100%);position:relative;padding-top:90px}
.bridal-title{text-align:center}
.bridal-title h2{font-family:"Libre Baskerville",serif;font-weight:400;font-size:32px;color:#222;letter-spacing:1px}
.bridal-title p{font-family:"Libre Baskerville",serif;font-size:17px;color:#222;margin-top:14px}
.bridal-title .stars{margin-top:14px}
.bridal-row{display:flex;gap:26px;width:1010px;margin:66px auto 0;position:relative;left:-2px}
.ring-card{width:233px;height:300px;background:#fff;border:1px solid var(--gold);padding-top:20px}
.ring-img{width:160px;height:150px;margin:0 auto;background:radial-gradient(circle,#cfcfcf 0%,#ededed 45%,#fff 65%)}
.ring-head{display:flex;justify-content:space-between;padding:14px 15px 0;font-family:"Montserrat",sans-serif;font-size:18px;font-weight:500}
.ring-head .price{color:var(--gold)}
.ring-desc{text-align:center;font-family:"Montserrat",sans-serif;font-size:13.5px;line-height:19px;color:#333;margin-top:25px}
.couple{position:absolute;right:150px;bottom:0;width:380px;height:340px;background:radial-gradient(ellipse at 50% 60%,#5a5a5a 0%,#8d8d8d 40%,rgba(154,154,154,0) 70%)}
.side-arrow{position:absolute;top:382px}

/* Footer */
.footer{height:395px;background:var(--dark);color:#fff}
.footer-cols{display:flex;width:1006px;margin:0 auto;padding-top:40px}
.fcol h4{font-weight:700;font-size:20px;display:inline-block;border-bottom:1px solid #fff;padding-bottom:4px;margin-bottom:22px}
.fcol-contact{width:257px;font-size:12.5px;line-height:19px}
.fcol-contact p.lead{text-align:justify;width:233px}
.contact-line{display:flex;gap:14px;margin-top:17px;align-items:flex-start}
.contact-line svg{flex:none;margin-top:2px}
.social{display:flex;gap:18px;margin:30px 0 0 48px}
.social span{width:14px;height:14px;border-radius:50%;background:#fff;display:block}
.fcol-links{width:257px;font-size:12.5px}
.links{display:grid;grid-template-columns:112px 120px;row-gap:10px}
.cards{display:flex;gap:8px;margin-top:40px}
.cards span{width:36px;height:24px;border-radius:3px;background:#e7e7e7;display:block}
.fcol-form{width:260px}
.field{width:231px;height:37px;border:1px solid #888;background:#fff;color:#999;font-size:12px;padding:10px 11px;margin:-2px 0 6px 2px}
.field.msg{height:105px}
.submit{width:231px;height:38px;background:var(--gold);color:#fff;text-align:center;line-height:38px;font-weight:700;font-size:15px;margin-left:2px}
.fcol-map{width:230px}
.map{width:230px;height:208px;background:linear-gradient(160deg,#f1efe9 0%,#e6e4dc 60%,#f3efe5 100%);border:1px solid #ddd}
.copyright{height:64px;background:var(--darker);color:#ccc;font-size:12.5px;text-align:center;line-height:64px}
</style>
</head>
<body>

<header class="topbar">
  <div class="wrap">
    <div class="contact">Contact us on (305)555-0192 or info@brillsjewelers-example.com</div>
    <div class="brand">
      <div class="brand-name">Brill's Jewelers</div>
      <div class="brand-tag">FINE JEWELRY · EST. 1958</div>
    </div>
    <div class="account"><span>Currency &#8964;</span><span>My Account</span><span>Checkout</span></div>
  </div>
</header>

<nav class="nav">
  <div class="wrap">
    <ul>
      <li>HOME</li>
      <li>ABOUT US<span class="caret"></span></li>
      <li>JEWELRY<span class="caret"></span></li>
      <li>DIAMONDS<span class="caret"></span></li>
      <li>SERVICES<span class="caret"></span></li>
      <li>CONTACT<span class="caret"></span></li>
    </ul>
    <div class="tools">
      <svg width="11" height="11" viewBox="0 0 12 12"><circle cx="5" cy="5" r="3.6" fill="none" stroke="#222" stroke-width="1.8"/><line x1="7.6" y1="7.6" x2="11" y2="11" stroke="#222" stroke-width="2"/></svg>
      <i></i>
      <svg width="12" height="11" viewBox="0 0 12 11"><path d="M6 10.5 1 5.5A2.7 2.7 0 0 1 6 2a2.7 2.7 0 0 1 5 3.5z" fill="#222"/></svg>
      <i></i>
      <svg width="12" height="11" viewBox="0 0 12 11"><path d="M0 1h2l1.5 6h6.5l1.5-4.5H3" fill="none" stroke="#222" stroke-width="1.4"/><circle cx="4.5" cy="9.5" r="1" fill="#222"/><circle cx="9" cy="9.5" r="1" fill="#222"/></svg>
      <span>0 item(s) - $0.00</span>
    </div>
  </div>
</nav>

<section class="hero">
  <div class="hero-art" role="img" aria-label="Two interlocking platinum solitaire diamond rings"></div>
  <div class="hero-copy">
    <h1>Celebrating our 45th year<br>on Palm Vista Way</h1>
    <a class="btn-outline">Shop Now</a>
  </div>
  <div class="arrow left"><svg width="12" height="18" viewBox="0 0 12 18"><path d="M9 2 3 9l6 7" fill="none" stroke="#fff" stroke-width="2"/></svg></div>
  <div class="arrow right"><svg width="12" height="18" viewBox="0 0 12 18"><path d="M3 2l6 7-6 7" fill="none" stroke="#fff" stroke-width="2"/></svg></div>
</section>

<section class="about">
  <div class="sec-title">
    <h2>ABOUT US</h2>
    <div class="stars"><svg width="40" height="10" viewBox="0 0 40 10"><g fill="#222"><path d="M5 0l1.5 3.3 3.5.4-2.6 2.4.7 3.5L5 7.8 1.9 9.6l.7-3.5L0 3.7l3.5-.4z"/><path d="M20 0l1.5 3.3 3.5.4-2.6 2.4.7 3.5L20 7.8l-3.1 1.8.7-3.5L15 3.7l3.5-.4z"/><path d="M35 0l1.5 3.3 3.5.4-2.6 2.4.7 3.5L35 7.8l-3.1 1.8.7-3.5L30 3.7l3.5-.4z"/></g></svg></div>
  </div>
  <div class="wrap about-body">
    <div class="about-photo" role="img" aria-label="Interior of the jewelry store with glass display cases"></div>
    <div class="about-text">
      <p>Brill's Jewelers is located in Palm Vista, Florida. The store has been family owned and operated since 1958.</p>
      <p>Thank you to our customers and friends!</p>
      <p>We are grateful for your patronage and loyalty over the past decades, helping you celebrate your special moments, and providing full jewelry services for you day in and day out.</p>
      <a class="btn-gold">Read More</a>
    </div>
  </div>
</section>

<section class="showcase">
  <div class="sec-title">
    <h2>SHOW STOPPERS</h2>
    <div class="stars"><svg width="40" height="10" viewBox="0 0 40 10"><g fill="#222"><path d="M5 0l1.5 3.3 3.5.4-2.6 2.4.7 3.5L5 7.8 1.9 9.6l.7-3.5L0 3.7l3.5-.4z"/><path d="M20 0l1.5 3.3 3.5.4-2.6 2.4.7 3.5L20 7.8l-3.1 1.8.7-3.5L15 3.7l3.5-.4z"/><path d="M35 0l1.5 3.3 3.5.4-2.6 2.4.7 3.5L35 7.8l-3.1 1.8.7-3.5L30 3.7l3.5-.4z"/></g></svg></div>
  </div>
  <div class="product-row">
    <article class="product">
      <div class="product-img" role="img" aria-label="Diamond halo engagement ring"></div>
      <div class="product-info"><div class="product-name">1218 Ring</div><div class="product-price">$259.00<s>$275.00</s></div></div>
      <div class="rating">★★★★☆</div>
    </article>
    <article class="product">
      <div class="product-img" role="img" aria-label="Pair of pearl stud earrings"></div>
      <div class="product-info"><div class="product-name">Diamond pearl</div><div class="product-price">$200.00</div></div>
      <div class="rating">★★★★☆</div>
    </article>
    <article class="product">
      <div class="product-img" role="img" aria-label="Emerald cut diamond halo ring"></div>
      <div class="product-info"><div class="product-name">Halo ring</div><div class="product-price">$320.00<s>$320.00</s></div></div>
      <div class="rating">★★★★★</div>
    </article>
    <article class="product">
      <div class="product-img gold" role="img" aria-label="Gold initial disc charm pendant"></div>
      <div class="product-info"><div class="product-name">Initial Disc Charm<br>Yellow</div><div class="product-price">$274.00</div></div>
      <div class="rating">★★★★★</div>
    </article>
  </div>
</section>

<section class="services light">
  <div class="sec-title">
    <h2>OUR SERVICES</h2>
    <div class="stars"><svg width="40" height="10" viewBox="0 0 40 10"><g fill="#fff"><path d="M5 0l1.5 3.3 3.5.4-2.6 2.4.7 3.5L5 7.8 1.9 9.6l.7-3.5L0 3.7l3.5-.4z"/><path d="M20 0l1.5 3.3 3.5.4-2.6 2.4.7 3.5L20 7.8l-3.1 1.8.7-3.5L15 3.7l3.5-.4z"/><path d="M35 0l1.5 3.3 3.5.4-2.6 2.4.7 3.5L35 7.8l-3.1 1.8.7-3.5L30 3.7l3.5-.4z"/></g></svg></div>
  </div>
  <div class="service-row">
    <div class="service">
      <div class="service-box">
        <svg width="96" height="84" viewBox="0 0 96 84" fill="none" stroke="#c9a24f" stroke-width="3"><path d="M22 66A34 34 0 1 1 74 66" stroke-dasharray="6 4"/><path d="M40 22v40M48 22v40M56 22v40"/><path d="M36 22h24"/></svg>
      </div>
      <h3>Repairs</h3>
    </div>
    <div class="service">
      <div class="service-box">
        <svg width="80" height="80" viewBox="0 0 80 80" fill="none" stroke="#c9a24f" stroke-width="3"><rect x="12" y="12" width="44" height="58"/><path d="M22 30h24M22 42h24M22 54h14"/><circle cx="34" cy="8" r="4"/><path d="M46 60l8 8 16-18"/></svg>
      </div>
      <h3>Appraisals</h3>
    </div>
    <div class="service">
      <div class="service-box">
        <svg width="96" height="90" viewBox="0 0 96 90" fill="none" stroke="#c9a24f" stroke-width="3"><path d="M18 70l14-24h40l-14 24z"/><path d="M32 46l8-12h38l-6 12"/><path d="M70 6l2 6 6 2-6 2-2 6-2-6-6-2 6-2z"/><path d="M28 12l1.5 4 4 1.5-4 1.5-1.5 4-1.5-4-4-1.5 4-1.5z"/></svg>
      </div>
      <h3>Buying Gold</h3>
    </div>
    <div class="service">
      <div class="service-box">
        <svg width="84" height="76" viewBox="0 0 84 76" fill="none" stroke="#c9a24f" stroke-width="3"><circle cx="30" cy="48" r="20"/><circle cx="54" cy="48" r="20"/><path d="M42 24l-8-8a5 5 0 0 1 8-6 5 5 0 0 1 8 6z"/></svg>
      </div>
      <h3>Custom</h3>
    </div>
  </div>
</section>

<section class="bridal" aria-label="Bridal collection">
  <div class="couple" role="img" aria-label="Couple sitting together on a beach, black and white"></div>
  <div class="bridal-title">
    <h2>Congratulations!</h2>
    <p>You found the girl now find her the ring</p>
    <div class="stars"><svg width="40" height="10" viewBox="0 0 40 10"><g fill="#222"><path d="M5 0l1.5 3.3 3.5.4-2.6 2.4.7 3.5L5 7.8 1.9 9.6l.7-3.5L0 3.7l3.5-.4z"/><path d="M20 0l1.5 3.3 3.5.4-2.6 2.4.7 3.5L20 7.8l-3.1 1.8.7-3.5L15 3.7l3.5-.4z"/><path d="M35 0l1.5 3.3 3.5.4-2.6 2.4.7 3.5L35 7.8l-3.1 1.8.7-3.5L30 3.7l3.5-.4z"/></g></svg></div>
  </div>
  <svg class="side-arrow" style="left:70px" width="12" height="20" viewBox="0 0 12 20"><path d="M10 2 3 10l7 8" fill="none" stroke="#111" stroke-width="2"/></svg>
  <svg class="side-arrow" style="left:1118px" width="12" height="20" viewBox="0 0 12 20"><path d="M2 2l7 8-7 8" fill="none" stroke="#111" stroke-width="2"/></svg>
  <div class="bridal-row">
    <article class="ring-card">
      <div class="ring-img" role="img" aria-label="Diamond halo ring with matching band"></div>
      <div class="ring-head"><span>67721</span><span class="price">$1,735</span></div>
      <div class="ring-desc">Diamond matching band,<br>3/8 ct tw, 14kt white</div>
    </article>
    <article class="ring-card">
      <div class="ring-img" role="img" aria-label="Oval diamond ring with matching band"></div>
      <div class="ring-head"><span>67799</span><span class="price">$1,735</span></div>
      <div class="ring-desc">Diamond matching band,<br>3/8 ct tw, 14kt white</div>
    </article>
    <article class="ring-card">
      <div class="ring-img" role="img" aria-label="Princess cut diamond ring with matching band"></div>
      <div class="ring-head"><span>68926</span><span class="price">$1,299</span></div>
      <div class="ring-desc">Diamond matching band,<br>1/4 ct tw, 14kt white</div>
    </article>
    <article class="ring-card">
      <div class="ring-img" role="img" aria-label="Marquise diamond ring with matching band"></div>
      <div class="ring-head"><span>68070</span><span class="price">$985</span></div>
      <div class="ring-desc">Diamond matching band,<br>1/6 ct tw, 14kt white</div>
    </article>
  </div>
</section>

<footer class="footer">
  <div class="footer-cols">
    <div class="fcol fcol-contact">
      <h4>Contact Us</h4>
      <p class="lead">Brill's Jewelers is located in Palm Vista, Florida. The store has been family owned and operated since 1958.</p>
      <div class="contact-line"><svg width="10" height="14" viewBox="0 0 10 14"><path d="M5 14S0 7.5 0 5a5 5 0 0 1 10 0c0 2.5-5 9-5 9z" fill="#a98436"/><circle cx="5" cy="5" r="1.8" fill="#262626"/></svg><span>418 Palm Vista Way, Palm Vista,<br>FL 39021</span></div>
      <div class="contact-line"><svg width="12" height="12" viewBox="0 0 12 12"><path d="M2.5 0 5 3 3.5 4.5a8 8 0 0 0 4 4L9 7l3 2.5-1.5 2C5 11.5.5 7 .5 1.5z" fill="#a98436"/></svg><span>(305)555-0192</span></div>
      <div class="contact-line"><svg width="13" height="10" viewBox="0 0 13 10"><rect width="13" height="10" fill="#a98436"/><path d="M0 0l6.5 5L13 0" fill="none" stroke="#262626" stroke-width="1.2"/></svg><span>info@brillsjewelers-example.com</span></div>
      <div class="social" aria-label="Social links"><span></span><span></span><span></span><span></span></div>
    </div>
    <div class="fcol fcol-links">
      <h4>Useful Links</h4>
      <div class="links">
        <a>Home</a><a>Store Locations</a>
        <a>About Us</a><a>Return Policy</a>
        <a>Services</a><a>My Account</a>
        <a>Jewelry</a><a>FAQs</a>
        <a>Diamonds</a><a>Terms &amp; Conditions</a>
        <a>Contact Us</a><a>Track Order</a>
      </div>
      <div class="cards" aria-label="Accepted payment methods"><span></span><span></span><span></span><span></span><span></span></div>
    </div>
    <div class="fcol fcol-form">
      <h4>Quick Contact</h4>
      <div class="field">Name...</div>
      <div class="field">Email...</div>
      <div class="field msg">Message...</div>
      <div class="submit">Submit</div>
    </div>
    <div class="fcol fcol-map">
      <h4>Locate Us</h4>
      <div class="map" role="img" aria-label="Street map showing the store location"></div>
    </div>
  </div>
</footer>
<div class="copyright">©Copyright information here</div>

</body>
</html>
```